Corporate Branding - Web and Print

A UK based company will like to use an existing logo to create branding materials for all marketing related documents, including business card, prints, letterhead, Website, Twitter, Facebook, Instagram logo etc. This company serves high-end clientele in the fashion, health and wellness and as such high quality and class is of utmost importance.
Where the logo can be modernised without losing its character then experiment. The main thing is to have a corporate branding which can be used later for brochures, Business Plan infographics.
The prominent colour within the organisation is burnt orange with no secondary colour. However if you believe a secondary colour is needed then use it, otherwise keep it simple and classy. Any chosen colours have to match perfectly.
Target Market(s)
High net worth individuals
Industry/Entity Type
Health And Wellness
Contact Information for Business Card
classy
Look and feel
Each slider illustrates characteristics of the customer's brand and the style your logo design should communicate.

```html
<!DOCTYPE html>
<html lang="en">
<head>
<meta charset="utf-8">
<title>Velmora Business Card</title>
<link rel="stylesheet" href="https://fonts.googleapis.com/css2?family=Open+Sans:wght@400;600;800&display=swap">
<style>
  :root {
    --backdrop: #3a3330;
    --card: #151515;
    --card-edge: #1e1e1e;
    --silver: #9a9a9a;
    --silver-soft: #7b7b7b;
    --orange: #f28c1e;
    --ink: #f2f2f2;
    --rule: #8a8a8a;
  }
  * { margin: 0; padding: 0; box-sizing: border-box; }
  html, body { width: 1200px; height: 864px; overflow: hidden; }
  body {
    background: var(--backdrop);
    font-family: "Open Sans", Arial, sans-serif;
    position: relative;
  }
  .card {
    position: absolute;
    width: 560px;
    height: 320px;
    background: var(--card);
    border: 1px solid var(--card-edge);
    box-shadow: 0 14px 30px rgba(0,0,0,0.45);
  }
  .card-front { left: 50px; top: 90px; }
  .card-back { left: 590px; top: 440px; }

  /* Front */
  .front-brand {
    position: absolute;
    left: 0; right: 0; top: 100px;
    display: flex; align-items: center; justify-content: center; gap: 16px;
  }
  .front-brand .mark-dot {
    width: 34px; height: 34px; border-radius: 50%;
    background: var(--silver);
  }
  .front-brand .brand-name {
    font-weight: 800; font-size: 58px; letter-spacing: 2px;
    color: var(--silver); line-height: 1;
  }
  .front-url {
    position: absolute; left: 0; right: 0; top: 214px;
    text-align: center; font-size: 14px; letter-spacing: 6px;
    color: var(--silver-soft);
  }

  /* Back */
  .back-brand {
    position: absolute; left: 36px; top: 128px;
    display: flex; align-items: center; gap: 12px;
  }
  .back-brand .mark-dot {
    width: 26px; height: 26px; border-radius: 50%; background: var(--orange);
  }
  .back-brand .brand-name {
    font-weight: 800; font-size: 44px; letter-spacing: 1px;
    color: var(--orange); line-height: 1;
  }
  .divider {
    position: absolute; left: 300px; top: 40px; width: 2px; height: 240px;
    background: linear-gradient(to bottom, transparent, var(--rule) 30%, var(--rule) 70%, transparent);
  }
  .contact {
    position: absolute; left: 322px; top: 58px;
    color: var(--ink); font-size: 15px; line-height: 1.35;
  }
  .contact .person-name {
    color: var(--orange); font-weight: 600; font-size: 17px; letter-spacing: 0.5px;
  }
  .contact .role { font-size: 15px; }
  .contact .address { margin-bottom: 2px; }
  .contact-line { display: flex; align-items: center; gap: 8px; }
  .contact-line svg { width: 13px; height: 13px; flex: none; fill: var(--orange); }
</style>
</head>
<body>
  <section class="card card-front">
    <div class="front-brand">
      <span class="mark-dot"></span>
      <span class="brand-name">VELMORA</span>
    </div>
    <p class="front-url">www.velmora.com</p>
  </section>

  <section class="card card-back">
    <div class="back-brand">
      <span class="mark-dot"></span>
      <span class="brand-name">VELMORA</span>
    </div>
    <div class="divider"></div>
    <div class="contact">
      <p class="person-name">ADRIAN HALE</p>
      <p class="role">CEO/FOUNDER</p>
      <p class="address">4120 Larkspur Road<br>Kingsbridge, Devon 58213</p>
      <p class="contact-line">
        <svg viewBox="0 0 16 16" aria-hidden="true"><path d="M3 1h3l1.5 4-2 1.2a9 9 0 0 0 4.3 4.3L11 8.5l4 1.5v3a2 2 0 0 1-2 2A12 12 0 0 1 1 3a2 2 0 0 1 2-2z"/></svg>
        541 206 7819
      </p>
      <p class="contact-line">
        <svg viewBox="0 0 16 16" aria-hidden="true"><path d="M4.5 0h7A1.5 1.5 0 0 1 13 1.5v13a1.5 1.5 0 0 1-1.5 1.5h-7A1.5 1.5 0 0 1 3 14.5v-13A1.5 1.5 0 0 1 4.5 0zM5 2v10h6V2zm3 11a1 1 0 1 0 0 2 1 1 0 0 0 0-2z"/></svg>
        702 315 4486
      </p>
      <p class="contact-line">
        <svg viewBox="0 0 16 16" aria-hidden="true"><path d="M4 1h7v4H4zM1 6h14v7h-3v2H4v-2H1zm4 5v3h6v-3z"/></svg>
        390 558 2173
      </p>
      <p class="contact-line">
        <svg viewBox="0 0 16 16" aria-hidden="true"><path d="M1 3h14v10H1zm1.5 1.5L8 9l5.5-4.5z"/></svg>
        adrian@velmora.com
      </p>
      <p class="contact-line">
        <svg viewBox="0 0 16 16" aria-hidden="true"><circle cx="8" cy="8" r="7"/></svg>
        www.velmora.com
      </p>
    </div>
  </section>
</body>
</html>
```